Design Our Full Stationary Set

Hi, I require a selection of complimentary stationary as outlined below. The winning design to be provided .eps and .svg of each. We are in the advertising sphere, the winning design should be artistic, colourful, attractive and grab your attention. Files attached.

All should be 300 DPI

Business Card - 2 Sides
Full Bleed Size 88x58mm (1040x685 pixels)
Safe Margin Size for Text 85x55mm (1004x650 pixels)

Folder
Full Bleed Size 53x42.4cm (6260x5004 pixels)
Safe Margin Size for Text 52.7x42.1cm (6225x4969 pixels)

Address Label
Full Bleed Size 90x52mm (1062x615 pixels)
Safe Margin Size for Text 87x49mm (1028x579 pixels)

Envelope Seal (CIRCLE)
Full Bleed Size 43mm diameter (510 pixels)
Safe Margin Size for Text 38mm diameter (450 pixels)

Letterhead
Full Bleed Size 213x300mm (2517x3544 pixels)
Safe Margin Size for Text 210x297mm (2480x3580 pixels)

INFORMATION:

Company Name: Vexley Quill Ltd.
Company Website: www.vexley-quill.example
Company No.: 7KQZ58
Address:
27 Bellwyn Court, Drumfiel, Kildare, Ireland, T8KN604.
Name: Colm Tierlan
Title: Chief Executive Officer
Email: ctierlan@vexley-quill.example
Phone: 00353-87-6209385

Target Market(s)

Advertisers and Marketers

Font styles to use
Serif
Script

Requirements
Must have
• Must fit dimensions given
Nice to have
• Colours that compliment our logo.

```html
<!DOCTYPE html>
<html lang="en">
<head>
<meta charset="utf-8">
<title>Vexley Quill Ltd. — Stationery Set</title>
<link rel="stylesheet" href="https://fonts.googleapis.com/css2?family=Raleway:wght@300;400&family=Open+Sans:wght@400;700&display=swap">
<style>
:root{
  --bg:#666a6c;
  --paper:#f7f7f7;
  --paper-tint:#e6e6e6;
  --ink:#2b2b2b;
  --ink-soft:#555;
  --green:#9dc13b;
  --green-deep:#5aa83a;
  --green-stripe:#8fb233;
  --red:#cf4b4f;
  --pink:#e0136f;
  --flap:#86c23a;
  --white:#ffffff;
}
*{box-sizing:border-box;margin:0;padding:0}
html,body{width:1200px;height:754px;overflow:hidden}
body{background:radial-gradient(ellipse at 45% 35%,#7a7e80 0%,var(--bg) 70%);position:relative;font-family:"Open Sans",sans-serif;color:var(--ink)}
.piece{position:absolute;overflow:hidden}
.pattern{position:absolute;border-radius:6px}
.pattern.paper{background:linear-gradient(160deg,var(--paper) 0%,var(--paper-tint) 100%)}
.pattern.bright{background:linear-gradient(125deg,var(--red) 0%,var(--green-deep) 100%);opacity:.85}
.wordmark{font-family:"Raleway",sans-serif;font-weight:300;letter-spacing:.12em;white-space:nowrap;display:flex;align-items:center;gap:.35em;position:absolute}
.wordmark .dot{display:inline-block;width:.55em;height:.55em;border-radius:50%;background:var(--red)}
.brand-hero{left:58px;top:80px;font-size:34px;color:var(--white)}

.letterhead{left:478px;top:87px;width:298px;height:393px;background:var(--paper)}
.letterhead .wordmark{right:38px;top:30px;font-size:15px;color:var(--ink)}
.letterhead .pattern{left:140px;top:226px;width:130px;height:132px}
.letter{position:absolute;left:38px;top:98px;width:222px;font-size:4.9px;line-height:1.3;color:var(--ink);z-index:1}
.letter p{margin-bottom:4px}
.signature{width:68px;height:12px;margin:6px 0 2px;background:linear-gradient(90deg,#cfcfcf,#e2e2e2)}
.letterhead .contact{position:absolute;left:0;right:0;bottom:11px;text-align:center;font-size:4.6px;color:var(--ink-soft);line-height:1.4}
.letterhead .band{position:absolute;bottom:0;left:0;height:4px;width:80%;background:var(--green)}
.letterhead .band.accent{left:80%;width:20%;background:var(--pink)}

.folder{left:805px;top:68px;width:330px;height:414px;background:var(--green)}
.folder .stripe{position:absolute;top:0;bottom:0;width:1px;background:var(--green-stripe)}
.folder .pattern{left:14px;top:222px;width:240px;height:160px}
.folder .wordmark{left:102px;top:38px;font-size:18px;color:var(--white)}
.folder .web{position:absolute;left:136px;top:391px;font-size:6.5px;color:var(--white)}

.card-front{left:278px;top:373px;width:149px;height:90px;background:var(--green);border-radius:4px}
.card-front .pattern{left:4px;top:3px;width:74px;height:52px}
.card-front .wordmark{right:12px;top:62px;font-size:11px;color:var(--white)}
.card-back{left:278px;top:488px;width:149px;height:86px;background:var(--paper);border-radius:4px}
.card-back .pattern{left:76px;top:18px;width:46px;height:46px}
.card-back .wordmark{left:10px;top:8px;font-size:11px;color:var(--ink)}
.card-back .person{position:absolute;left:11px;top:36px;font-size:4.2px;line-height:1.35;color:var(--ink);z-index:1}
.card-back .name{color:var(--green);font-weight:700;font-size:5px;letter-spacing:.05em}
.card-back .role{margin-bottom:2px}
.card-back .line{display:flex;align-items:center;gap:2px}
.card-back .line i{width:3px;height:3px;border-radius:50%;background:var(--green);display:inline-block}
.card-back .address{margin-top:2px}

.envelope-front{left:479px;top:519px;width:314px;height:148px;background:var(--paper)}
.envelope-front .pattern{left:14px;top:18px;width:122px;height:120px}
.envelope-front .wordmark{right:24px;top:20px;font-size:13px;color:var(--ink)}
.envelope-back{left:830px;top:519px;width:313px;height:148px;background:var(--paper)}
.envelope-back .flap{position:absolute;left:0;top:0;width:100%;height:52px}
.envelope-back .return{position:absolute;left:0;right:0;bottom:9px;text-align:center;font-size:3.8px;color:var(--ink)}
</style>
</head>
<body>

<div class="wordmark brand-hero">VEXLEY QUILL<span class="dot"></span></div>

<section class="piece letterhead" aria-label="Letterhead">
  <div class="pattern paper" role="img" aria-label="Faint grey decorative pattern area"></div>
  <div class="wordmark">VEXLEY QUILL<span class="dot"></span></div>
  <div class="letter">
    <p>March 7, 2016<br>Mr. Ronan Hale<br>88 Copper Mill Road<br>Hartfield, U.K 40517</p>
    <p>Dear Mr. Hale<br>The first paragraph of a typical business letter is used to state the main point of the letter. Begin with a friendly opening; then quickly transition into the purpose of your letter. Use a couple of sentences to explain the purpose, but do not go in to detail until the next paragraph.</p>
    <p>Beginning with the second paragraph, state the supporting details to justify your purpose. These may take the form of background information, statistics or first-hand accounts. A few short paragraphs within the body of the letter should be enough to support your reasoning.</p>
    <p>Finally, in the closing paragraph, briefly restate your purpose and why it is important. If the purpose of your letter is related to your employment, consider ending your letter with your contact information and title if it is not included on letterhead. However, if the purpose is informational, think about closing with gratitude for the reader's time.</p>
    <p>These may take the form of background information, statistics or first-hand accounts. A few short paragraphs within the body of the letter should be enough to support your reasoning.</p>
    <p>Sincerely,</p>
    <div class="signature" role="img" aria-label="Handwritten signature of Colm Tierlan"></div>
    <p>Owner</p>
  </div>
  <div class="contact">00353-87-6209385<br>ctierlan@vexley-quill.example | www.vexley-quill.example</div>
  <div class="band"></div><div class="band accent"></div>
</section>

<section class="piece folder" aria-label="Presentation folder">
  <div class="stripe" style="left:6px"></div>
  <div class="stripe" style="left:11px"></div>
  <div class="pattern bright" role="img" aria-label="Colourful decorative pattern area in red and green"></div>
  <div class="wordmark">VEXLEY QUILL<span class="dot"></span></div>
  <div class="web">www.vexley-quill.example</div>
</section>

<section class="piece card-front" aria-label="Business card front">
  <div class="pattern bright" role="img" aria-label="Colourful decorative pattern area in red and green"></div>
  <div class="wordmark">VEXLEY QUILL<span class="dot"></span></div>
</section>

<section class="piece card-back" aria-label="Business card back">
  <div class="pattern paper" role="img" aria-label="Faint grey decorative pattern area"></div>
  <div class="wordmark">VEXLEY QUILL<span class="dot"></span></div>
  <div class="person">
    <div class="name">COLM TIERLAN</div>
    <div class="role">Chief Executive Officer</div>
    <div class="line"><i></i>00353-87-6209385</div>
    <div class="line"><i></i>ctierlan@vexley-quill.example</div>
    <div class="line"><i></i>www.vexley-quill.example</div>
    <div class="address">27 Bellwyn Court, Drumfiel, Kildare, Ireland, T8KN604.</div>
  </div>
</section>

<section class="piece envelope-front" aria-label="Envelope front">
  <div class="pattern paper" role="img" aria-label="Faint grey decorative pattern area"></div>
  <div class="wordmark">VEXLEY QUILL<span class="dot"></span></div>
</section>

<section class="piece envelope-back" aria-label="Envelope back">
  <svg class="flap" viewBox="0 0 313 52" preserveAspectRatio="none" aria-hidden="true">
    <path d="M0 0H313V6L306 46Q305 52 298 52H15Q8 52 7 46L0 6Z" fill="var(--flap)"/>
  </svg>
  <div class="return">Unit 12, Larkmoor Yard, Box 4417, Drumfiel | t: +353 1 555 0142 | e: info@larkmoor.example | w: www.larkmoor.example</div>
</section>

</body>
</html>
```